iOS developer portal page

We need a web design for a company based in Beijing called BrightNook. Our company develops an SDK used by iOS developers making children's educational apps. The SDK provides cross-promotional marketing, user analytics, teacher feedback and activities, and parent reports for developers who implement it.
Our company offers a product that benefits parents and developers, however the design we need is in regard to the landing page for developers using our product.Developers using our SDK are mostly based in the USA and develop apps for the USA Orchard Tunebox store.
There is an included wireframe for the first design idea. Design comps can be similar or different from the wireframe, however it should be considered as a good starting point for the final design.
Updates
Thank you for the design submissions. We are currently reviewing the designs internally and will notify all designers once a decision has been reached.
Kind regards,
Merrick
Project Deadline Extended
Reason: The deadline is being extended by one day so it will be closed at the end of the business week. Thank you.
Target Market(s)
iOS Developers for Children's education apps
Industry/Entity Type
It Company
Look and feel
Each slider illustrates characteristics of the customer's brand and the style your logo design should communicate.

```html
<!DOCTYPE html>
<html lang="en">
<head>
<meta charset="utf-8">
<title>BrightNook — SDK for Children's Education Apps</title>
<link rel="stylesheet" href="https://fonts.googleapis.com/css2?family=Arimo:wght@400;700&display=swap">
<style>
:root{
  --green:#5aab14;
  --red:#d0162f;
  --ink:#333;
  --muted:#555;
  --slate:#3e4a5e;
  --panel:#f2f2f3;
  --panel-first:#e0e3e9;
  --rule:#9a9a9a;
  --blue:#1e9ad6;
  --releases-top:#3b5aa3;
  --releases-mid:#5373bd;
  --card:#e9e9eb;
  --nav-top:#4a4a4a;
  --nav-bottom:#141414;
  --signup:#1ea0e0;
}
*{box-sizing:border-box;margin:0;padding:0}
html,body{width:923px;height:1200px;overflow:hidden;background:#fff}
body{position:relative;font-family:"Arimo",Arial,sans-serif;color:var(--ink)}
.abs{position:absolute}

.hero-photo{left:0;top:0;width:923px;height:470px;
  background:linear-gradient(90deg,#cfd3d8 0%,#e8dfe0 22%,#f3d9df 36%,#f7eef0 52%,#ffffff 66%,#ffffff 100%)}
.brand{left:26px;top:52px;font-size:32px;font-weight:700;color:var(--green);letter-spacing:-.5px}
.brand-beta{left:190px;top:46px;font-size:8px;color:#888}

.main-nav{left:442px;top:48px;width:467px;height:55px;border-radius:8px;display:flex;
  background:linear-gradient(#5a5a5a,var(--nav-top) 40%,var(--nav-bottom));box-shadow:0 1px 3px rgba(0,0,0,.4)}
.main-nav a{display:flex;align-items:center;justify-content:center;color:#fff;font-weight:700;font-size:14px;
  text-decoration:none;border-right:1px solid #0c0c0c;box-shadow:1px 0 0 #5c5c5c;text-shadow:0 1px 1px #000}
.main-nav a:last-child{border-right:0;box-shadow:none}

.headline{left:592px;top:142px;font-size:40px;color:var(--green);line-height:1}
.headline-strong{left:592px;top:195px;font-size:44px;color:var(--red);line-height:1}
.hero-copy{left:605px;top:260px;width:288px;font-size:11px;line-height:18.3px;color:var(--muted);text-align:justify}

.signup{left:760px;top:390px;width:134px;height:50px}
.signup-pill{left:30px;top:6px;width:102px;height:38px;border-radius:19px;background:linear-gradient(#6fcdf5,var(--signup) 55%,#1388c7);
  color:#fff;font-weight:700;font-size:19px;display:flex;align-items:center;justify-content:center;padding-left:14px;box-shadow:0 1px 2px rgba(0,0,0,.3)}
.signup svg{position:absolute;left:0;top:0}

.features{left:14px;top:472px;width:879px;height:288px;background:var(--panel);border:1px solid #d7d7d7;
  box-shadow:0 2px 5px rgba(0,0,0,.25);display:flex}
.feature{position:relative;padding:18px 14px 0;width:218px}
.feature:first-child{background:var(--panel-first);width:216px}
.feature + .feature::before{content:"";position:absolute;left:0;top:20px;height:252px;border-left:1px solid var(--rule)}
.feature:nth-child(2)::before{display:none}
.feature-head{display:flex;align-items:center;gap:12px;height:42px;font-size:15px;font-weight:700;color:var(--slate);line-height:20px}
.feature p{margin-top:22px;font-size:11px;line-height:16.6px;text-align:justify;color:#222}
.feature .more{position:absolute;right:14px;top:252px;font-size:13px;color:var(--slate)}

.press{left:15px;top:780px;width:375px;height:155px;background:var(--red);border-radius:3px;color:#fff}
.press-badge{position:absolute;left:9px;top:13px;width:146px;height:68px;background:#fff;display:flex;align-items:center;justify-content:center;
  font-size:23px;color:#1a5c9a}
.press-title{position:absolute;left:164px;top:22px;font-size:23px;line-height:27px}
.press p{position:absolute;left:13px;top:95px;width:352px;font-size:11px;line-height:16.5px}

.testimonials-title{left:411px;top:793px;font-size:18px;font-weight:700;color:var(--blue)}
.testimonial-author{left:422px;top:893px;font-size:12px;font-weight:700;color:#555;line-height:16px}
.testimonial-quote{left:524px;top:836px;width:354px;font-size:11px;line-height:17px;color:#666;text-align:justify}

.releases{left:23px;top:955px;width:879px;height:168px;border-radius:4px;
  background:linear-gradient(90deg,var(--releases-top),var(--releases-mid) 50%,var(--releases-top))}
.releases h2{position:absolute;left:16px;top:13px;font-size:18px;color:#fff}
.release{position:absolute;top:55px;width:222px;height:88px;background:var(--card);border-radius:3px}
.release-art{position:absolute;left:6px;top:7px;width:72px;height:72px;border-radius:14px}
.release h3{position:absolute;left:86px;top:17px;font-size:15px;font-weight:400;color:#222}
.release span{position:absolute;left:86px;font-size:11px;color:#222}
.slider-arrow{position:absolute;top:84px}

.footer-copy{left:17px;top:1163px;font-size:11px;color:#222}
.social{top:1160px;width:21px;height:21px;border-radius:2px}
</style>
</head>
<body>

<div class="abs hero-photo" role="img" aria-label="Photo of a young girl lying on a bed, chin in hand, looking at a laptop"></div>
<div class="abs brand">BrightNook</div>
<div class="abs brand-beta">Beta</div>

<nav class="abs main-nav">
  <a href="#" style="width:88px">Home</a>
  <a href="#" style="width:98px">About Us</a>
  <a href="#" style="width:76px">News</a>
  <a href="#" style="width:93px">Support</a>
  <a href="#" style="width:112px">Contact Us</a>
</nav>

<div class="abs headline">Make Your Apps</div>
<div class="abs headline-strong">IRRESISTABLE</div>
<p class="abs hero-copy">Many desktop publishing packages and web page editors now use Lorem Ipsum as their default model text, and a search for 'lorem ipsum' will uncover many web sites still in their infancy. Various versions have evolved over the years, sometimes by accident, sometimes on purpose (injected humour and the like).</p>

<a class="abs signup" href="#">
  <span class="abs signup-pill">Sign Up</span>
  <svg width="42" height="50" viewBox="0 0 42 50">
    <path d="M11 24v-8a10 10 0 0 1 20 0v8" fill="none" stroke="#9a9a9a" stroke-width="5"/>
    <rect x="4" y="23" width="34" height="24" rx="4" fill="#c9c9c9" stroke="#8a8a8a"/>
    <circle cx="21" cy="33" r="3" fill="#666"/>
  </svg>
</a>

<section class="abs features">
  <div class="feature">
    <div class="feature-head">
      <svg width="26" height="26" viewBox="0 0 26 26"><circle cx="13" cy="13" r="11" fill="none" stroke="#222" stroke-width="2.5"/><path d="M13 2a11 11 0 0 0 0 22z" fill="#222"/></svg>
      Parent Report</div>
    <p>The standard chunk of Lorem Ipsum used since the 1500s is reproduced below for those interested. Sections 1.10.32 and 1.10.33 from "de Finibus Bonorum et Malorum" by Cicero are also reproduced in their exact original form, accompanied by English versions from the 1914 translation by H. Rackham. The first line of Lorem Ipsum, comes from a line.</p>
    <a class="more">View more ›</a>
  </div>
  <div class="feature">
    <div class="feature-head">
      <svg width="26" height="24" viewBox="0 0 26 24"><rect x="1" y="12" width="4" height="11" fill="#222"/><rect x="7" y="8" width="4" height="15" fill="#222"/><rect x="13" y="3" width="4" height="20" fill="#222"/><rect x="19" y="10" width="4" height="13" fill="#222"/></svg>
      Cross - Promotional Marketing</div>
    <p>The standard chunk of Lorem Ipsum used since the 1500s is reproduced below for those interested. Sections 1.10.32 and 1.10.33 from "de Finibus Bonorum et Malorum" by Cicero are also reproduced in their exact original form, accompanied by English versions from the 1914 translation by H. Rackham. The first line of Lorem Ipsum, comes from a line.</p>
    <a class="more">View more ›</a>
  </div>
  <div class="feature">
    <div class="feature-head">
      <svg width="26" height="26" viewBox="0 0 26 26"><path d="M14 4H3v19h19V12" fill="none" stroke="#222" stroke-width="2.5"/><path d="M10 16l2-5 10-10 3 3-10 10z" fill="#222"/></svg>
      Teacher Feedback &amp; Activities</div>
    <p>The standard chunk of Lorem Ipsum used since the 1500s is reproduced below for those interested. Sections 1.10.32 and 1.10.33 from "de Finibus Bonorum et Malorum" by Cicero are also reproduced in their exact original form, accompanied by English versions from the 1914 translation by H. Rackham. The first line of Lorem Ipsum, comes from a line.</p>
    <a class="more">View more ›</a>
  </div>
  <div class="feature">
    <div class="feature-head">
      <svg width="28" height="24" viewBox="0 0 28 24"><path d="M2 1v21h25" fill="none" stroke="#222" stroke-width="2.5"/><path d="M5 16l6-7 5 5 9-9" fill="none" stroke="#222" stroke-width="2.5"/></svg>
      User Analytics</div>
    <p>The standard chunk of Lorem Ipsum used since the 1500s is reproduced below for those interested. Sections 1.10.32 and 1.10.33 from "de Finibus Bonorum et Malorum" by Cicero are also reproduced in their exact original form, accompanied by English versions from the 1914 translation by H. Rackham. The first line of Lorem Ipsum, comes from a line.</p>
    <a class="more">View more ›</a>
  </div>
</section>

<section class="abs press">
  <div class="press-badge">TechPulse</div>
  <div class="press-title">BrightNook featured in TechPulse</div>
  <p>Sections 1.10.32 and 1.10.33 from "de Finibus Bonorum et Malorum" by Cicero are also reproduced in their exact original form, accompanied by English versions from the 1914 translation by H. Rackham.</p>
</section>

<h2 class="abs testimonials-title">Testimonials</h2>
<svg class="abs" style="left:421px;top:830px" width="54" height="54" viewBox="0 0 54 54">
  <circle cx="27" cy="17" r="12" fill="#6b6b6b"/>
  <path d="M4 54c0-16 10-24 23-24s23 8 23 24z" fill="#6b6b6b"/>
</svg>
<div class="abs testimonial-author">Marla<br>Mother of Two</div>
<p class="abs testimonial-quote">The standard chunk of Lorem Ipsum used since the 1500s is reproduced below for those interested. Sections 1.10.32 and 1.10.33 from "de Finibus Bonorum et Malorum" by Cicero are also reproduced in their exact original form, accompanied by English versions from the 1914 translation by H. Rackham.</p>

<section class="abs releases">
  <h2>Recent Releases</h2>
  <svg class="slider-arrow" style="left:18px" width="22" height="32" viewBox="0 0 22 32"><path d="M18 2L4 16l14 14" fill="none" stroke="#fff" stroke-width="4"/></svg>
  <div class="release" style="left:70px">
    <div class="release-art" role="img" aria-label="App icon illustration of a penguin astronaut" style="background:linear-gradient(#9fb6c8,#5d7890)"></div>
    <h3>This Weeks Words</h3><span style="top:42px">by Quillmoor</span><span style="top:59px">FREE</span>
  </div>
  <div class="release" style="left:338px">
    <div class="release-art" role="img" aria-label="App icon illustration of a panda" style="background:linear-gradient(#dfe8d6,#a9c48f)"></div>
    <h3>This Weeks Words</h3><span style="top:42px">by Quillmoor</span><span style="top:59px">FREE</span>
  </div>
  <div class="release" style="left:597px">
    <div class="release-art" role="img" aria-label="App icon illustration of a yellow bee character" style="background:linear-gradient(#e6dcf0,#b9a3d4)"></div>
    <h3>This Weeks Words</h3><span style="top:42px">by Quillmoor</span><span style="top:59px">FREE</span>
  </div>
  <svg class="slider-arrow" style="left:842px" width="22" height="32" viewBox="0 0 22 32"><path d="M4 2l14 14L4 30" fill="none" stroke="#fff" stroke-width="4"/></svg>
</section>

<footer>
  <div class="abs footer-copy">Copyright © 2011 www.brightnook.com &nbsp;&nbsp; All rights reserved</div>
  <span class="abs social" style="left:742px;background:#3b5998"></span>
  <span class="abs social" style="left:778px;background:#4aa8d8"></span>
  <span class="abs social" style="left:815px;background:#f0792b"></span>
  <span class="abs social" style="left:852px;background:#1a73a8"></span>
  <span class="abs social" style="left:890px;background:#9a9a9a"></span>
</footer>

</body>
</html>
```